K7 Maplewave Consulting Group Ltd - Website Design

We already have a company logo. We need a website created for our consulting agency.
Refer to attached files for logo and website content.
We would also be open to any additional recommendations.
Industry/Entity Type
Finance And Accounting
Coding
Coded - Design and coding required
Number of Pages Required
1 page
Font styles to use
Serif
Colors
3377b5
b868aa
33b8a4
Requirements
Must have
- Company Logo, name and who we are.

```html
<!DOCTYPE html>
<html lang="en">
<head>
<meta charset="utf-8">
<title>K7 Maplewave Consulting Group Ltd</title>
<link href="https://fonts.googleapis.com/css2?family=Catamaran:wght@500;600;700;800&family=Poppins:wght@400;500;600&display=swap" rel="stylesheet">
<style>
:root{
  --navy:#2a1f6b;
  --ink:#333;
  --teal:#33b8a4;
  --blue:#0a75bc;
  --brand-blue:#3377b5;
  --pink:#b868aa;
  --footer:#252b35;
  --footer-text:#b8bec8;
  --white:#fff;
}
*{margin:0;padding:0;box-sizing:border-box}
html,body{width:1200px;height:3540px;overflow:hidden;background:var(--white)}
body{position:relative;font-family:"Poppins",sans-serif;color:var(--ink)}
.abs{position:absolute}
.head{font-family:"Catamaran",sans-serif}

/* header */
.site-header{top:0;left:0;width:1200px;height:109px;background:var(--white);box-shadow:0 1px 4px rgba(0,0,0,.08);z-index:2}
.brand{left:48px;top:12px;width:200px;color:var(--navy);font-weight:400;text-align:center;white-space:nowrap}
.brand .mark{display:block;width:40px;height:40px;border-radius:50%;border:2px solid var(--navy);margin:0 auto 4px}
.brand .name{font-size:22px;line-height:26px;letter-spacing:.3px}
.brand .sub{font-size:7px;letter-spacing:.5px;line-height:10px}
.call{left:755px;top:18px;font-size:18px;color:var(--navy);display:flex;align-items:center;gap:10px}
.call b{font-weight:500}
.live{left:996px;top:14px;width:119px;height:33px;border-radius:17px;background:var(--brand-blue);color:#fff;font-size:11px;font-weight:500;display:flex;align-items:center;justify-content:center;gap:6px}
.nav{top:68px;left:667px;display:flex;gap:40px;font-size:18px;color:#222}

/* hero */
.hero-photo{top:109px;left:0;width:1200px;height:541px;background:linear-gradient(100deg,#d9cfc4 0%,#c9b9a4 30%,#8a6d5a 55%,#a3463f 70%,#d5c9bd 85%,#8c97a4 100%)}
.hero-shade{top:109px;left:0;width:700px;height:541px;background:linear-gradient(90deg,rgba(240,236,230,.85),rgba(240,236,230,0))}
.hero-title{left:122px;top:230px;font-size:46px;font-weight:700;color:var(--navy);line-height:52px}
.hero-sub{left:122px;top:296px;font-size:27px;font-weight:700;color:var(--navy);line-height:34px}
.hero-text{left:122px;top:352px;font-size:22px;line-height:33px;color:#3a3a3a;font-weight:500;font-family:"Catamaran",sans-serif}
.btn-pink{left:124px;top:456px;width:196px;height:50px;border-radius:25px;background:var(--pink);color:#fff;font-size:18px;display:flex;align-items:center;justify-content:center;gap:12px;font-family:"Catamaran",sans-serif;font-weight:500}
.hero-next{left:1064px;top:330px;width:60px;height:60px;border-radius:50%;background:rgba(40,60,100,.55);display:flex;align-items:center;justify-content:center}
.scroll{left:590px;top:600px;width:20px;height:32px;border:2px solid #fff;border-radius:10px}

/* services */
.sec-title{width:1200px;left:0;text-align:center;font-family:"Catamaran",sans-serif;font-weight:700;color:var(--navy);line-height:1}
.services-title{top:808px;font-size:48px}
.card{width:312px;height:253px;background:#fff;border:1px solid #ddd;box-shadow:0 2px 5px rgba(0,0,0,.15);text-align:center}
.card .icon{position:absolute;left:109px;top:-43px;width:94px;height:94px;border-radius:50%;background:var(--teal);display:flex;align-items:center;justify-content:center}
.card h3{margin-top:72px;font-family:"Catamaran",sans-serif;font-size:18px;font-weight:600;color:var(--navy);text-transform:uppercase}
.card p{margin:6px auto 0;width:240px;font-size:12.5px;line-height:19px;color:#444;font-family:"Catamaran",sans-serif}
.card .more{display:inline-block;margin-top:16px;width:151px;height:40px;border:2px solid #888;border-radius:20px;font-family:"Catamaran",sans-serif;font-size:15px;font-weight:600;line-height:37px;color:#444}

/* why */
.why-band{top:1672px;left:0;width:1200px;height:613px;background:var(--blue)}
.why-title{left:115px;top:1840px;font-size:46px;line-height:46px;font-weight:700;color:#fff}
.why-text{left:115px;top:1908px;width:450px;font-size:17.5px;line-height:24px;color:#fff;font-family:"Catamaran",sans-serif;font-weight:500}
.btn-outline{left:115px;top:2055px;width:169px;height:50px;border:3px solid #fff;border-radius:25px;color:#fff;font-family:"Catamaran",sans-serif;font-weight:700;font-size:18px;display:flex;align-items:center;justify-content:center}
.why-frame{left:645px;top:1834px;width:436px;height:330px;border:5px solid #fff;border-radius:6px}
.why-photo{left:613px;top:1794px;width:440px;height:344px;background:linear-gradient(135deg,#c9b28e 0%,#e8e2d8 40%,#2b3a55 65%,#cfd3d8 100%)}

/* testimonial */
.testi-title{top:2402px;font-size:46px;left:20px}
.underline{left:560px;top:2458px;width:120px;height:4px;background:var(--navy)}
.testi-card{left:364px;top:2527px;width:480px;height:222px;background:#fff;box-shadow:0 4px 18px rgba(0,0,0,.1);text-align:center}
.testi-card p{margin:60px auto 0;width:300px;font-size:14px;line-height:24px;color:#444}
.testi-card .who{margin-top:8px;font-family:"Catamaran",sans-serif;font-size:22px;font-weight:500;color:var(--navy)}
.quote{left:594px;top:2498px}
.avatar{left:261px;top:2473px;width:163px;height:163px;border-radius:50%;background:radial-gradient(circle at 50% 45%,#d8b49a,#8a9aa8);border:4px solid #fff;box-shadow:0 2px 8px rgba(0,0,0,.15)}
.arrow-btn{top:2702px;width:48px;height:48px;display:flex;align-items:center;justify-content:center}
.arrow-prev{left:797px;background:#fff;box-shadow:0 2px 6px rgba(0,0,0,.12)}
.arrow-next{left:845px;background:var(--teal)}

/* appointment */
.appoint-band{top:2860px;left:0;width:1200px;height:311px;background:var(--teal)}
.appoint-title{top:2928px;width:1200px;left:0;text-align:center;font-size:54px;line-height:54px;font-weight:800;color:#fff;letter-spacing:-1px}
.appoint-text{top:2992px;width:1200px;left:0;text-align:center;font-size:12.5px;line-height:16px;font-weight:700;color:#fff;font-family:"Catamaran",sans-serif}
.field{top:3044px;width:223px;height:41px;background:#fff;font-size:14px;color:#666;padding-left:16px;line-height:41px;font-family:"Catamaran",sans-serif}
.submit{left:857px;top:3044px;width:207px;height:41px;background:var(--brand-blue);color:#fff;font-family:"Catamaran",sans-serif;font-weight:700;font-size:15px;display:flex;align-items:center;justify-content:center}

/* footer */
.footer{top:3171px;left:0;width:1200px;height:369px;background:var(--footer)}
.foot-brand{left:113px;top:3236px;width:244px;color:#fff;text-align:center;font-weight:400;white-space:nowrap}
.foot-brand .mark{display:block;width:50px;height:50px;border-radius:50%;border:2px solid #fff;margin:0 auto 8px}
.foot-brand .name{font-size:28px;line-height:34px}
.foot-brand .sub{font-size:9px;letter-spacing:.5px}
.copy{left:133px;top:3386px;font-size:14px;color:var(--footer-text)}
.social{top:3439px;width:32px;height:32px;border:1.5px solid var(--footer-text);border-radius:50%}
.foot-h{top:3254px;font-size:17px;font-weight:600;color:var(--footer-text);letter-spacing:.5px}
.links{left:544px;top:3298px;list-style:none;font-size:14.5px;line-height:27px;color:var(--footer-text)}
.news-text{left:725px;top:3298px;width:360px;font-size:14px;line-height:21px;color:var(--footer-text)}
.news-input{left:725px;top:3366px;width:310px;height:48px;border:2px solid #555c68;border-radius:24px;overflow:hidden;display:flex}
.news-input span{flex:1;padding-left:26px;line-height:44px;font-size:15px;color:var(--footer-text)}
.news-input b{width:113px;background:#3a414d;color:#fff;font-weight:400;font-size:15px;line-height:44px;text-align:center}
.schedule{left:725px;top:3440px;width:310px;height:46px;border-radius:23px;background:var(--brand-blue);color:#fff;font-family:"Catamaran",sans-serif;font-weight:600;font-size:15px;display:flex;align-items:center;justify-content:center}
</style>
</head>
<body>

<header class="abs site-header">
  <div class="abs brand"><span class="mark"></span><div class="name">K7 MAPLEWAVE</div><div class="sub">CONSULTING GROUP LTD</div></div>
  <div class="abs call">
    <svg width="22" height="22" viewBox="0 0 24 24" fill="none" stroke="#333" stroke-width="1.6"><path d="M5 3h4l2 5-2.5 1.5a11 11 0 0 0 6 6L16 13l5 2v4a2 2 0 0 1-2 2A16 16 0 0 1 3 5a2 2 0 0 1 2-2z"/></svg>
    <span>Call us : <b>555-014270</b></span>
  </div>
  <div class="abs live"><svg width="14" height="13" viewBox="0 0 14 13"><path d="M1 1h12v8H6l-3 3V9H1z" fill="#fff"/></svg>LIVE CHAT</div>
  <nav class="abs nav"><span>Home</span><span>About Us</span><span>Services</span><span>Blog</span><span>Contact</span></nav>
</header>

<section class="hero">
  <div class="abs hero-photo" role="img" aria-label="Photo of a young couple reviewing financial documents with an advisor"></div>
  <div class="abs hero-shade"></div>
  <h1 class="abs head hero-title">FINANCIAL PLANNERS</h1>
  <div class="abs head hero-sub">WE HELP BUSINESS INNOVATE AND GROW</div>
  <div class="abs hero-text">Specialized services for small and<br>medium sized enterprises</div>
  <div class="abs btn-pink">Our Services
    <svg width="30" height="12" viewBox="0 0 30 12" fill="none" stroke="#fff" stroke-width="1.5"><path d="M0 6h28M23 1l5 5-5 5"/></svg>
  </div>
  <div class="abs hero-next"><svg width="20" height="30" viewBox="0 0 20 30" fill="none" stroke="#fff" stroke-width="3"><path d="M5 3l11 12L5 27"/></svg></div>
  <div class="abs scroll"></div>
</section>

<section class="services">
  <h2 class="abs sec-title services-title">Services Offered?</h2>
  <div class="abs card" style="left:106px;top:950px"><div class="icon"><svg width="44" height="44" viewBox="0 0 44 44" fill="none" stroke="#fff" stroke-width="2"><circle cx="22" cy="17" r="9"/><path d="M22 12v10M19 15h5M5 34l8-4h10l9-5 4 3-14 10H5"/></svg></div><h3>Accounting</h3><p>Lorem Ipsum is simply dummy text of the printing and typesetting industry. Lorem Ipsum has been</p><span class="more">LEARN MORE</span></div>
  <div class="abs card" style="left:443px;top:950px"><div class="icon"><svg width="44" height="44" viewBox="0 0 44 44" fill="none" stroke="#fff" stroke-width="2"><rect x="10" y="5" width="24" height="34" rx="2"/><path d="M15 13h14M15 19h14M15 25h14M15 31h9"/></svg></div><h3>Bookkeeping</h3><p>Lorem Ipsum is simply dummy text of the printing and typesetting industry. Lorem Ipsum has been</p><span class="more">LEARN MORE</span></div>
  <div class="abs card" style="left:781px;top:950px"><div class="icon"><svg width="44" height="44" viewBox="0 0 44 44" fill="none" stroke="#fff" stroke-width="2"><circle cx="22" cy="15" r="9"/><path d="M22 10v10M6 30l8-5 8 6 8-6 8 5-8 8-8-5-8 5z"/></svg></div><h3>Financial Management</h3><p>Lorem Ipsum is simply dummy text of the printing and typesetting industry. Lorem Ipsum has been</p><span class="more">LEARN MORE</span></div>
  <div class="abs card" style="left:106px;top:1274px"><div class="icon"><svg width="44" height="44" viewBox="0 0 44 44" fill="none" stroke="#fff" stroke-width="2"><rect x="9" y="5" width="24" height="32" rx="3"/><path d="M14 13h14M14 19h14M14 25h6M24 32l4 4 8-9"/></svg></div><h3>Government Grants</h3><p>Lorem Ipsum is simply dummy text of the printing and typesetting industry. Lorem Ipsum has been</p><span class="more">LEARN MORE</span></div>
  <div class="abs card" style="left:443px;top:1274px"><div class="icon"><svg width="44" height="44" viewBox="0 0 44 44" fill="none" stroke="#fff" stroke-width="2"><rect x="17" y="17" width="10" height="10"/><circle cx="10" cy="10" r="3"/><circle cx="34" cy="10" r="3"/><circle cx="10" cy="34" r="3"/><circle cx="34" cy="34" r="3"/><circle cx="22" cy="7" r="3"/><circle cx="22" cy="37" r="3"/><path d="M12 12l5 5M32 12l-5 5M12 32l5-5M32 32l-5-5M22 10v7M22 27v7"/></svg></div><h3>Strategy</h3><p>Lorem Ipsum is simply dummy text of the printing and typesetting industry. Lorem Ipsum has been</p><span class="more">LEARN MORE</span></div>
  <div class="abs card" style="left:781px;top:1274px"><div class="icon"><svg width="44" height="44" viewBox="0 0 44 44" fill="none" stroke="#fff" stroke-width="2"><rect x="5" y="7" width="34" height="24" rx="2"/><path d="M16 37h12M22 31v6"/><rect x="10" y="12" width="8" height="5"/><rect x="20" y="12" width="8" height="5"/><rect x="10" y="20" width="8" height="5"/><rect x="20" y="20" width="14" height="5"/></svg></div><h3>Mergers and Acquisitions</h3><p>Lorem Ipsum is simply dummy text of the printing and typesetting industry. Lorem Ipsum has been</p><span class="more">LEARN MORE</span></div>
</section>

<section class="why">
  <div class="abs why-band"></div>
  <h2 class="abs head why-title">Why Choose Us</h2>
  <p class="abs why-text">Lorem Ipsum is simply dummy text of the printing and typesetting industry. Lorem Ipsum has been industry's standard dummy text ever since the 1500s, when an unknown printer took a galley of type and scrambled.</p>
  <div class="abs btn-outline">LEARN MORE</div>
  <div class="abs why-frame"></div>
  <div class="abs why-photo" role="img" aria-label="Photo of hands using a calculator beside a notebook on a desk"></div>
</section>

<section class="testimonial">
  <h2 class="abs sec-title testi-title">Client Testimonial</h2>
  <div class="abs underline"></div>
  <div class="abs testi-card"><p>Lorem ipsum dolor sit amet, consectetur adipiscing elit, sed do eiusmod tempor incididunt ut labore et dolore magna dolore aliqua.</p><div class="who">Dara Quill</div></div>
  <svg class="abs quote" width="54" height="46" viewBox="0 0 54 46" fill="none" stroke="#2a1f6b" stroke-width="2"><path d="M4 44V24C4 12 10 5 22 3M4 24h18v20H4M30 44V24c0-12 6-19 18-21M30 24h18v20H30"/></svg>
  <div class="abs avatar" role="img" aria-label="Portrait photo of the client"></div>
  <div class="abs arrow-btn arrow-prev"><svg width="10" height="14" viewBox="0 0 10 14" fill="none" stroke="#111" stroke-width="3"><path d="M8 1L2 7l6 6"/></svg></div>
  <div class="abs arrow-btn arrow-next"><svg width="10" height="14" viewBox="0 0 10 14" fill="none" stroke="#fff" stroke-width="3"><path d="M2 1l6 6-6 6"/></svg></div>
</section>

<section class="appointment">
  <div class="abs appoint-band"></div>
  <h2 class="abs head appoint-title">MAKE AN APPOINTMENT</h2>
  <p class="abs appoint-text">Lorem Ipsum is simply dummy text of the printing and typesetting industry. Lorem Ipsum has been</p>
  <div class="abs field" style="left:165px">Name</div>
  <div class="abs field" style="left:396px">Phone</div>
  <div class="abs field" style="left:627px">Email address</div>
  <div class="abs submit">MAKE AN APPOINTMENT</div>
</section>

<footer>
  <div class="abs footer"></div>
  <div class="abs foot-brand"><span class="mark"></span><div class="name">K7 MAPLEWAVE</div><div class="sub">CONSULTING GROUP LTD</div></div>
  <p class="abs copy">© 2021 K7 Maplewave. All Rights are Reserved.</p>
  <span class="abs social" style="left:136px" aria-label="Social link"></span>
  <span class="abs social" style="left:175px" aria-label="Social link"></span>
  <span class="abs social" style="left:214px" aria-label="Social link"></span>
  <span class="abs social" style="left:254px" aria-label="Social link"></span>
  <h4 class="abs foot-h" style="left:544px">QUICK LINKS</h4>
  <ul class="abs links"><li>Home</li><li>About Us</li><li>Services</li><li>Blog</li><li>Team</li><li>How its works</li><li>Contact Us</li></ul>
  <h4 class="abs foot-h" style="left:725px">SIGN UP FOR NEWSLETTER</h4>
  <p class="abs news-text">If you are interested in joining our class, or have any questions please send us a message.</p>
  <div class="abs news-input"><span>Email address</span><b>Subscribe</b></div>
  <div class="abs schedule">SCHEDULE FREE 15 MIN CONSULTATION</div>
</footer>

</body>
</html>
```